We are having a Bright Dawn, Bold Self Reshape Challenge at our fitness studio. We need a poster design using the template attached as a reference. I have also included our Vorabloom logo to put on the poster. Please DO NOT use the graphics in the flyer as we are expecting something much better :-)

-Size needed 11x17 with bleeding for printing

-We need this made in Photoshop (CS3 friendly) or at least delivered in PS as we might change some text or re-arrange the design later on.

-We need this in layers.

```html
<!DOCTYPE html>
<html lang="en">
<head>
<meta charset="utf-8">
<title>Vorabloom Bootcamps – Bright Dawn, Bold Self Reshape Challenge</title>
<link rel="stylesheet" href="https://fonts.googleapis.com/css2?family=Roboto+Condensed:wght@400;700&family=Oswald:wght@500;600&display=swap">
<style>
  :root {
    --poster-black: #121314;
    --poster-charcoal: #2a2c2f;
    --photo-mid: #4a4c4f;
    --photo-dark: #1b1c1e;
    --headline-silver: #e6e3ea;
    --accent-orange: #c97b2c;
    --text-white: #ffffff;
    --badge-blue: #2c4ea0;
    --badge-blue-light: #4c74c8;
    --ribbon-red: #d8242a;
    --band-blue: #2f55a8;
    --band-blue-edge: #1d3a7e;
  }
  * { margin: 0; padding: 0; box-sizing: border-box; }
  html, body { width: 800px; height: 1200px; overflow: hidden; background: var(--poster-black); }
  .poster {
    position: relative;
    width: 800px; height: 1200px;
    background: linear-gradient(180deg, var(--poster-charcoal) 0%, var(--poster-black) 45%, var(--poster-black) 100%);
    font-family: "Roboto Condensed", "Arial Narrow", sans-serif;
    color: var(--text-white);
    overflow: hidden;
  }
  .athlete-photo {
    position: absolute; left: 0; top: 585px; width: 800px; height: 525px;
    background: radial-gradient(ellipse 55% 60% at 42% 45%, var(--photo-mid) 0%, var(--photo-dark) 70%, var(--poster-black) 100%);
  }
  .brand {
    position: absolute; top: 70px; left: 0; width: 800px;
    text-align: center;
  }
  .brand-name {
    display: inline-flex; align-items: center; gap: 16px;
    font-family: "Oswald", sans-serif; font-weight: 600;
    font-size: 64px; letter-spacing: 2px; text-transform: uppercase;
    color: var(--text-white); line-height: 1;
  }
  .brand-mark { width: 34px; height: 34px; background: var(--accent-orange); }
  .brand-tagline {
    margin-top: 14px; font-size: 20px; font-weight: 700;
    letter-spacing: 4px; text-transform: uppercase; color: var(--headline-silver);
  }
  .headline { position: absolute; top: 248px; left: 0; width: 800px; text-align: center; text-transform: uppercase; }
  .headline-kicker {
    font-family: "Oswald", sans-serif; font-weight: 600; font-size: 44px;
    color: var(--headline-silver); line-height: 1.1;
  }
  .headline-main {
    font-family: "Oswald", sans-serif; font-weight: 600; font-size: 56px;
    color: var(--headline-silver); line-height: 1.15;
  }
  .subhead {
    position: absolute; top: 398px; left: 0; width: 800px;
    text-align: center; font-size: 23px; line-height: 34px;
  }
  .schedule {
    position: absolute; top: 470px; left: 0; width: 800px;
    text-align: center; font-size: 28px; line-height: 38px;
  }
  .schedule dt { display: inline; color: var(--accent-orange); font-weight: 700; }
  .schedule dd { display: inline; }
  .offer {
    position: absolute; top: 622px; right: 78px;
    text-align: right; font-weight: 700; font-size: 31px; line-height: 42px;
  }
  .offer-price { font-size: 42px; }
  .prize-badge { position: absolute; left: 530px; top: 790px; width: 196px; height: 190px; }
  .info-band {
    position: absolute; left: 0; top: 1110px; width: 800px; height: 54px;
    background: linear-gradient(90deg, var(--band-blue-edge) 0%, var(--band-blue) 20%, var(--band-blue) 80%, var(--band-blue-edge) 100%);
    display: flex; align-items: center; justify-content: center;
    font-size: 26px; font-weight: 700;
  }
</style>
</head>
<body>
<main class="poster">
  <div class="athlete-photo" role="img" aria-label="Athlete in a ponytail and workout gear doing a one-arm push-up on a dark studio floor"></div>

  <header class="brand">
    <div class="brand-name"><span class="brand-mark"></span>Vorabloom Bootcamps</div>
    <p class="brand-tagline">The Ultimate Fitness Solution</p>
  </header>

  <h1 class="headline">
    <span class="headline-kicker">Bright Dawn, Bold Self</span><br>
    <span class="headline-main">Reshape Challenge</span>
  </h1>

  <p class="subhead">In Just 6 Weeks, Transform Your Body And<br>Get In The Best Shape Of Your Life!</p>

  <dl class="schedule">
    <div><dt>Kick Off Meeting:</dt> <dd>Thursday, Jan 14 at 7:30 pm</dd></div>
    <div><dt>Start Date:</dt> <dd>Monday, January 18th</dd></div>
    <div><dt>End Date:</dt> <dd>Friday, February 26th</dd></div>
  </dl>

  <p class="offer">6 Weeks of Training,<br>Nutrition, and Coaching<br>Starting at just <span class="offer-price">$99!</span></p>

  <svg class="prize-badge" viewBox="0 0 196 190" aria-label="$500 prize for winner">
    <circle cx="98" cy="88" r="86" fill="var(--badge-blue)"/>
    <circle cx="98" cy="88" r="74" fill="var(--text-white)"/>
    <circle cx="98" cy="88" r="66" fill="var(--badge-blue-light)"/>
    <circle cx="98" cy="88" r="66" fill="none" stroke="var(--badge-blue)" stroke-width="6"/>
    <text x="98" y="98" text-anchor="middle" font-family="Oswald, sans-serif" font-weight="600" font-size="46" fill="var(--text-white)">$500</text>
    <polygon points="0,118 22,118 22,146 0,146 10,132" fill="#9e1a1f"/>
    <polygon points="196,118 174,118 174,146 196,146 186,132" fill="#9e1a1f"/>
    <rect x="14" y="112" width="168" height="30" fill="var(--ribbon-red)"/>
    <text x="98" y="134" text-anchor="middle" font-family="Roboto Condensed, sans-serif" font-weight="700" font-size="18" fill="var(--text-white)">PRIZE FOR WINNER!</text>
  </svg>

  <footer class="info-band">Visit www.vorabloombootcamps.com FOR MORE INFO</footer>
</main>
</body>
</html>
```